Honey Meadow Bake Shop site. I'm opening up a shop in a few months and I have ideas of what I want,

I would like a wordpress design that is mobile friendly. I want to be able to easily add and remove photos when necessary. I want to be able to display my home, about us, contact us, instagram photos, and my menu. I need to eventually include the days and hours the store will be open. I would like to also include the instagram and FB symbol (I know there is a name for it, not sure) that will take you directly to the site.

Please look at the following sites. I like the simplicity of it. I've attached a picture below that shows how I told my logo designer I would like my font.

https://www.cornerplatekitchen.com/
https://www.thebrightcrumbs.com/
http://www.maplelanebakehouse.com/
Below is my instagram page

https://www.instagram.com/honeymeadowbakeshop/

Target Market(s)

All ages

Industry/Entity Type

Bakery

Coding

Coded - Design and coding required

Font styles to use
Serif
Sans Serif

Colors
9d9d9d
757575
474747
fbd4d5

Requirements
Must have
• I've attached my updated logo. Please use it when making the website. Thank you. Keep colors simple. Remember, my bakery is going to have a rustic theme. I've attached my "About Us", please include. I crossed out what I don't want included. Thanks!! :)
Nice to have
• See websites I've attached for ideas. Can't wait to see some designs! Clean borders for pictures, preferably squares. I like the pink, but please, I don't want it to be all you see. Very minimal. I could see some designs without as well. Think rustic chic, simple, elegant. Hope that helps!
Should not have
• I don't want my website to look exactly like the examples. :) No scallop edges. I do not sell online.

```html
<!DOCTYPE html>
<html lang="en">
<head>
<meta charset="utf-8">
<title>Honey Meadow Bake Shop — Our Menu</title>
<link href="https://fonts.googleapis.com/css2?family=Libre+Caslon+Text:ital,wght@0,400;1,400&family=Libre+Caslon+Display&family=Montserrat:wght@400;500;600&display=swap" rel="stylesheet">
<style>
:root{
  --ink:#2f2f2f;
  --text:#474747;
  --muted:#757575;
  --line:#9d9d9d;
  --blush:#fbd4d5;
  --blush-soft:#fdeceb;
  --sky:#e4f8fa;
  --white:#ffffff;
  --serif:"Libre Caslon Text", Georgia, serif;
  --display:"Libre Caslon Display", Georgia, serif;
  --sans:"Montserrat", Arial, sans-serif;
}
*{box-sizing:border-box;margin:0;padding:0}
html,body{width:1200px;height:3529px;overflow:hidden;background:var(--white);color:var(--text);font-family:var(--serif)}
.page{position:relative;width:1200px;height:3529px}
.abs{position:absolute}

.notice-bar{left:0;top:0;width:1200px;height:28px;background:var(--blush-soft);font:500 10px/28px var(--sans);text-align:center;color:var(--text)}
.notice-bar u{text-decoration:underline}

.social{left:0;top:64px;width:1200px;display:flex;justify-content:center;gap:22px}
.social span{width:9px;height:9px;border-radius:50%;background:var(--text)}

.brand{left:0;top:98px;width:1200px;text-align:center}
.brand-name{font:400 42px/1 var(--display);color:var(--ink)}
.brand-sub{font:500 12px/1 var(--sans);letter-spacing:6px;color:var(--muted);margin-top:10px}

.main-nav{left:0;top:185px;width:1200px;display:flex;justify-content:center;font:500 11px/16px var(--sans);color:var(--ink)}
.main-nav a{padding:0 20px;border-left:1px solid var(--line);color:inherit;text-decoration:none}
.main-nav a:first-child{border-left:0}

.contact-line{left:0;top:214px;width:1200px;display:flex;justify-content:center;gap:30px;font:400 9px/14px var(--sans);letter-spacing:.5px;color:var(--text)}
.contact-line span{display:flex;align-items:center;gap:6px}

.page-title{left:0;top:268px;width:1200px;text-align:center;font:400 78px/1 var(--display);color:var(--ink)}
.intro{left:0;top:374px;width:1200px;text-align:center;font:400 16px/26px var(--serif);color:var(--ink)}
.btn{display:inline-block;background:var(--blush);font:600 8px/1 var(--sans);letter-spacing:1.5px;color:var(--ink);padding:6px 14px}
.brochure{left:0;top:464px;width:1200px;text-align:center}

.menu-card{left:313px;top:546px;width:576px;height:807px;background:var(--blush-soft);border:1px solid #e6c9ca;outline:1px solid #e6c9ca;outline-offset:4px}
.menu-card h2{position:absolute;left:53px;top:70px;font:400 32px/1 var(--display);color:var(--ink);white-space:nowrap}
.menu-card .rule{position:absolute;left:352px;top:87px;width:216px;height:1px;background:var(--ink)}
.menu-card .prices{position:absolute;left:53px;top:114px;font:600 7.5px/1 var(--sans);letter-spacing:.4px;color:var(--ink)}
.cake-col{position:absolute;top:150px;width:214px}
.cake-col.left{left:53px}
.cake-col.right{left:294px;width:222px}
.cake{margin-bottom:13px}
.cake h3{font:400 14.5px/19px var(--serif);color:var(--ink);white-space:nowrap}
.cake h3 i{font-size:12px}
.cake p{font:400 9.5px/12px var(--sans);color:var(--text)}

.list-col{top:1384px}
.list-col h4{font:500 14px/18px var(--sans);color:var(--ink);white-space:nowrap}
.list-col .note{font:600 6.5px/9px var(--sans);letter-spacing:.3px;color:var(--ink);margin:4px 0 12px;width:120px}
.list-col ul{list-style:none}
.list-col li{font:400 12px/16px var(--serif);color:var(--ink);margin-bottom:6px}
.list-col.tight li{margin-bottom:0;line-height:17px;white-space:nowrap}
.list-col li i{font-size:11px}
.donuts{left:310px;width:190px}
.cupcake-box{left:529px;top:1381px;width:161px;height:137px;background:var(--sky);padding:13px 12px}
.cupcake-box h4{font:500 15px/18px var(--sans);color:var(--ink)}
.cupcake-box p{font:400 11px/13px var(--serif);color:var(--ink);margin-top:9px}
.cookies{left:529px;top:1536px;width:180px}
.bars{left:720px;width:180px}
.bars .group + .group{margin-top:28px}

.host{left:310px;top:2000px;width:579px;height:675px;background:var(--blush-soft)}
.polaroid{position:absolute;background:var(--white);padding:10px 10px 40px;box-shadow:0 4px 12px rgba(0,0,0,.18)}
.polaroid .photo{width:100%;height:100%}
.p1{left:565px;top:1902px;width:148px;height:196px;transform:rotate(-8deg)}
.p2{left:672px;top:1966px;width:162px;height:210px;transform:rotate(6deg)}
.p3{left:608px;top:2118px;width:98px;height:112px;transform:rotate(-12deg);padding:7px 7px 24px}
.p1 .photo{background:linear-gradient(135deg,#8a8a8a,#d9c7b3 55%,#5d6d7c)}
.p2 .photo{background:linear-gradient(160deg,#cfc3b3,#efe6da 50%,#a89580)}
.p3 .photo{background:linear-gradient(135deg,#b7864f,#f1ddc3)}

.host h2{position:absolute;left:37px;top:200px;font:400 36px/42px var(--display);color:var(--ink)}
.host .lede{position:absolute;left:37px;top:296px;width:420px;font:400 14px/19px var(--serif);color:var(--ink)}
.event-form{position:absolute;left:37px;top:394px;width:352px}
.field{background:var(--white);height:26px;font:600 7px/26px var(--sans);letter-spacing:.5px;color:var(--ink);padding-left:8px;position:relative}
.row{display:flex;gap:10px;margin-bottom:10px}
.row .field{flex:1}
.field.select::after{content:"";position:absolute;right:10px;top:11px;border:4px solid transparent;border-top-color:var(--ink)}
.field.area{height:108px;line-height:20px;padding-top:2px}
.submit{margin-top:18px;width:112px;height:16px;background:var(--blush);font:600 7.5px/16px var(--sans);letter-spacing:2px;text-align:center;color:var(--ink)}

.insta-band{left:310px;top:2753px;width:579px;height:235px;background:var(--sky)}
.insta-title{left:0;top:2798px;width:1200px;text-align:center;font:400 25px/30px var(--display);color:var(--ink)}
.insta-grid{left:341px;top:2904px;width:518px;display:grid;grid-template-columns:repeat(3,166px);gap:10px}
.insta-grid div{height:166px}
.g1{background:linear-gradient(135deg,#3a2c22,#d59a52 50%,#f2e3cc)}
.g2{background:linear-gradient(135deg,#7a6a5c,#e8dccf 50%,#c2b09c)}
.g3{background:linear-gradient(135deg,#e9d9c4,#c98b5a 50%,#f4c6cc)}
.g4{background:linear-gradient(135deg,#2b2b2f,#b98653 50%,#6c5a4a)}
.g5{background:linear-gradient(135deg,#f0e6dc,#b34a3c 50%,#e8c9a0)}
.g6{background:linear-gradient(135deg,#4a3b32,#f1e8dc 50%,#c9a27a)}

.quote{left:0;top:3332px;width:1200px;text-align:center;font:400 17px/22px var(--serif);color:var(--ink)}
.copyright{left:0;top:3420px;width:1200px;text-align:center;font:400 8px/1 var(--sans);color:var(--muted)}
.hours-bar{left:0;top:3505px;width:1200px;height:24px;background:var(--sky);display:flex;justify-content:center;align-items:center;gap:28px;font:400 10px/1 var(--serif);color:var(--ink)}
.hours-bar b{font:600 7px/1 var(--sans);letter-spacing:.8px}
</style>
</head>
<body>
<div class="page">

  <div class="abs notice-bar">We offer our cupcakes, donuts and bars in bite size for events. All orders require 48 hours notice. For larger orders, <u>please email</u> or call ahead. Thank you!</div>

  <div class="abs social" aria-label="Social links"><span></span><span></span><span></span></div>

  <header class="abs brand">
    <div class="brand-name">Honey Meadow</div>
    <div class="brand-sub">BAKE SHOP</div>
  </header>

  <nav class="abs main-nav">
    <a href="#">Menu</a><a href="#">Order Inquiry</a><a href="#">Gallery</a><a href="#">About</a>
  </nav>

  <div class="abs contact-line">
    <span><svg width="8" height="11" viewBox="0 0 8 11"><path d="M4 0a4 4 0 0 0-4 4c0 3 4 7 4 7s4-4 4-7a4 4 0 0 0-4-4zm0 5.5A1.5 1.5 0 1 1 4 2.5a1.5 1.5 0 0 1 0 3z" fill="#474747"/></svg>214 Orchard Lane, Fairbrook, CT 06100</span>
    <span><svg width="10" height="10" viewBox="0 0 10 10"><path d="M2 0l2 2.5-1.2 1.3a6 6 0 0 0 3.4 3.4L7.5 6 10 8l-1.5 2C4 10 0 6 0 1.5z" fill="#474747"/></svg>203-555-0142</span>
    <span><svg width="11" height="8" viewBox="0 0 11 8"><rect x=".5" y=".5" width="10" height="7" fill="none" stroke="#474747"/><path d="M.5.5l5 4 5-4" fill="none" stroke="#474747"/></svg>info@honeymeadowbakeshop.com</span>
  </div>

  <h1 class="abs page-title">Our Menu</h1>
  <p class="abs intro">Everything we bake is made with the freshest and finest ingredients,<br>including <i>Valleroux Cocoa</i> and natural fruits.</p>
  <div class="abs brochure"><span class="btn">DOWNLOAD OUR BROCHURE</span></div>

  <section class="abs menu-card">
    <h2>Honey Meadow Cakes</h2>
    <div class="rule"></div>
    <div class="prices">6" 4 LAYER CAKE $45 ✱SPECIALTY CAKE $45 &nbsp;•&nbsp; 8" 3 LAYER CAKE $55 ✱SPECIALTY CAKE $60</div>
    <div class="cake-col left">
      <div class="cake"><h3>Chocolate Salted Caramel*</h3><p>Moist chocolate cake frosted with salted caramel buttercream and salted caramel drizzle</p></div>
      <div class="cake"><h3>Red Velvet</h3><p>Classic southern red velvet cake frosted with cream cheese buttercream</p></div>
      <div class="cake"><h3>Cookies &amp; Cream</h3><p>Moist chocolate cake frosted with salted caramel buttercream and salted caramel drizzle</p></div>
      <div class="cake"><h3>Classic Vanilla Bean</h3><p>Moist chocolate cake frosted with salted caramel buttercream and salted caramel drizzle</p></div>
      <div class="cake"><h3>Chocolate Cake</h3><p>Moist chocolate cake frosted with chocolate or vanilla buttercream</p></div>
      <div class="cake"><h3>Hummingbird*</h3><p>Banana, pecan and pineapple cake frosted with brown buttercream</p></div>
      <div class="cake"><h3>Classic Carrot</h3><p>Carrot cake with cinnamon cream cheese buttercream</p></div>
      <div class="cake"><h3>Sticky Toffee Pudding*</h3><p>Date cake frosted with mascarpone whipped cream, and topped with toffee sauce</p></div>
    </div>
    <div class="cake-col right">
      <div class="cake"><h3>Banana</h3><p>Banana cake frosted with cinnamon brown buttercream</p></div>
      <div class="cake"><h3>Strawberry*</h3><p>Fresh strawberry cake frosted with strawberry buttercream</p></div>
      <div class="cake"><h3>Banana</h3><p>Banana cake frosted with cinnamon brown buttercream</p></div>
      <div class="cake"><h3>Vanilla Chocolate</h3><p>Vanilla cake frosted with vanilla buttercream and topped with ganache</p></div>
      <div class="cake"><h3>Funfetti</h3><p>Vanilla cake filled with sprinkles and frosted with sprinkle vanilla buttercream</p></div>
      <div class="cake"><h3>Lemon</h3><p>Lemon cake filled with lemon curd filling and frosted with lemon buttercream</p></div>
      <div class="cake"><h3>Pumpkin <i>(seasonal)</i>*</h3><p>Vanilla cake filled with sprinkles and frosted with sprinkle vanilla buttercream</p></div>
      <div class="cake"><h3>Eggnog <i>(seasonal)</i></h3><p>Vanilla cake frosted with eggnog buttercream</p></div>
      <div class="cake"><h3>Gingerbread <i>(seasonal)</i></h3><p>Ginger spice cake frosted with cream cheese buttercream</p></div>
    </div>
  </section>

  <section class="abs list-col donuts">
    <h4>Cake donuts $2,25/EA</h4>
    <p class="note">MUST BE ORDERED BY THE DOZEN PER FLAVOR</p>
    <ul>
      <li>Vanilla with vanilla glaze, topped with sprinkles</li>
      <li>Vanilla with chocolate ganache, topped with chocolate sprinkles</li>
      <li>Blueberry with cinnamon glaze</li>
      <li>Chai with chai glaze</li>
      <li>Strawberry with strawberry glaze</li>
      <li>Coconut with coconut glaze and topped with shredded coconut</li>
      <li>Red velvet with cream cheese glaze</li>
      <li>Pumpkin with cream cheese glaze <i>(seasonal)</i></li>
      <li>Snickerdoodle with cinnamon sugar</li>
    </ul>
  </section>

  <section class="abs cupcake-box">
    <h4>Cupcakes<br>$3.00/EA<br>$33/DOZEN</h4>
    <p>Same flavors as cakes above Must be ordered by the dozen per flavor</p>
  </section>

  <section class="abs list-col tight cookies">
    <h4>Cookies $2,25/EA</h4>
    <p class="note">MUST BE ORDERED BY THE DOZEN PER FLAVOR</p>
    <ul>
      <li>Chocolate Chip</li><li>Oatmeal</li><li>Snickerdoodle</li><li>Chai</li>
      <li>Sugar cookies with sprinkles</li><li>Gingerbread <i>(seasonal)</i></li>
      <li>Pumpkin spice <i>(seasonal)</i></li><li>Shortbread</li>
    </ul>
  </section>

  <section class="abs list-col tight bars">
    <div class="group">
      <h4>Bars $2.75/EA</h4>
      <p class="note">MUST BE ORDERED BY THE DOZEN PER FLAVOR</p>
      <ul>
        <li>Brownie</li><li>Snickerdoodle blondie bar</li><li>S'mores bar</li>
        <li>Brookie bar <i>(Brownie &amp; Cookie)</i></li><li>Lemon bar</li><li>Apple pie bar</li>
        <li>Strawberry bar</li><li>Pumpkin pie bar <i>(seasonal)</i></li>
      </ul>
    </div>
    <div class="group">
      <h4>Confections $0,75/EA</h4>
      <p class="note">MUST BE ORDERED BY THE DOZEN PER FLAVOR</p>
      <ul>
        <li>Fluffy</li><li>Marshmallows</li><li>Vanilla</li><li>Chocolate Toasted</li><li>Coconut</li><li>Strawberry</li>
      </ul>
    </div>
  </section>

  <section class="abs host">
    <h2>Being the host<br>was never so easy</h2>
    <p class="lede">Whether it's a birthday, shower, engagement, wedding, corporate event, we aim to make it a delightful and decadent experience filled with love and joy.</p>
    <div class="event-form">
      <div class="row"><div class="field">FULL NAME</div><div class="field">EMAIL ADDRESS</div></div>
      <div class="row"><div class="field">PHONE NUMBER</div><div class="field select">TYPE OF EVENTS</div></div>
      <div class="field area">TELL US ABOUT YOUR EVENT</div>
      <div class="submit">SUBMIT</div>
    </div>
  </section>
  <div class="polaroid p1"><div class="photo" role="img" aria-label="Instant photo of a wedding couple"></div></div>
  <div class="polaroid p2"><div class="photo" role="img" aria-label="Instant photo of a frosted celebration cake"></div></div>
  <div class="polaroid p3"><div class="photo" role="img" aria-label="Instant photo of baked treats"></div></div>

  <div class="abs insta-band"></div>
  <h2 class="abs insta-title">Follow me on instagram<br>for more bites</h2>
  <div class="abs insta-grid">
    <div class="g1" role="img" aria-label="Cupcakes with caramel frosting"></div>
    <div class="g2" role="img" aria-label="Glazed scones on parchment"></div>
    <div class="g3" role="img" aria-label="Frosted bars with sprinkles"></div>
    <div class="g4" role="img" aria-label="Chocolate chip cookies on a cooling rack"></div>
    <div class="g5" role="img" aria-label="Strawberry crumble bars"></div>
    <div class="g6" role="img" aria-label="Slice of pie on a plate"></div>
  </div>

  <p class="abs quote">“Ô The joy of bringing sheer delight to the<br>experience of enjoying yummy treats”</p>
  <p class="abs copyright">©2017 Honey Meadow Bake Shop. All rights reserved.</p>

  <footer class="abs hours-bar">
    <b>OPENING TIME</b><span>Monday - Friday &nbsp;8:30 AM TO 6:45 PM</span><span>Saturday &nbsp;8:30 AM TO 1:00 PM</span>
  </footer>

</div>
</body>
</html>
```